Stationery and Biz Cards for a Publishing Solutions Company
Bram Keswick Publishing Solutions, LLC
Simple
Lyle R. Pennock
President/Managing Editor
478 Birchfield Hollow Road
Valencia, PA 16874
lyle.pennock@bramkeswickbooks.example
www.bramkeswickbooks.example
Here is the company logo.

```html
<!DOCTYPE html>
<html lang="en">
<head>
<meta charset="utf-8">
<title>Bram Keswick Publishing Solutions — Stationery</title>
<link href="https://fonts.googleapis.com/css2?family=Cinzel:wght@500&family=Open+Sans:wght@400;600&display=swap" rel="stylesheet">
<style>
  :root{
    --stage:#2c2c2e;
    --paper:#ffffff;
    --paper-shade:#eef0f3;
    --navy:#14185a;
    --royal:#2a3aa8;
    --bright:#3d5ad8;
    --silver:#c9ccd2;
    --slate:#4a4c52;
    --ink:#2a2d4a;
    --muted:#8a8d99;
    --rule:#b9bcc6;
  }
  *{box-sizing:border-box;margin:0;padding:0}
  html,body{width:1200px;height:523px;overflow:hidden;background:var(--stage)}
  body{position:relative;font-family:"Open Sans",Arial,sans-serif;color:var(--ink)}
  .piece{position:absolute;overflow:hidden;background:var(--paper);box-shadow:0 3px 8px rgba(0,0,0,.45)}
  .piece svg.band{position:absolute;left:0;width:100%;display:block}

  .brand{position:absolute;display:flex;align-items:center;gap:4px;font-family:"Cinzel",Georgia,serif;font-weight:500;color:var(--navy);white-space:nowrap;letter-spacing:.04em}
  .brand .mark{display:block;background:var(--navy)}
  .brand.light{color:#fff}
  .brand.light .mark{background:#fff}

  /* business cards */
  .card{width:200px;height:82px}
  .card-front{left:36px;top:24px}
  .card-back{left:248px;top:44px;width:214px;height:78px}
  .card-navy{left:30px;top:112px;background:linear-gradient(135deg,var(--navy),var(--royal));transform:rotate(-1deg)}
  .card-slate{left:244px;top:126px;width:214px;height:76px;background:linear-gradient(135deg,#3a3c42,#5b5d63)}
  .contact{position:absolute;left:10px;top:8px;font-size:5.4px;line-height:1.45;color:var(--ink)}
  .contact strong{font-weight:600;font-size:6px}
  .tagline{position:absolute;font-size:4.5px;letter-spacing:.12em;text-transform:uppercase}

  /* envelopes */
  .env{width:266px;height:92px}
  .env-plain{left:22px;top:242px}
  .env-slate{left:156px;top:308px;width:272px;height:104px;background:#5a5c62}
  .env-return{left:42px;top:424px}
  .return{position:absolute;left:12px;bottom:12px;font-size:5px;line-height:1.4;color:var(--ink)}

  /* letterhead */
  .letterhead{left:426px;top:24px;width:388px;height:520px}
  .watermark{position:absolute;left:0;right:0;top:220px;text-align:center;font-family:"Cinzel",Georgia,serif;font-weight:500;font-size:30px;color:var(--paper-shade);letter-spacing:.08em}

  /* fax */
  .fax{left:830px;top:24px;width:360px;height:520px}
  .fax-title{position:absolute;right:26px;top:100px;font-weight:600;font-size:13px;letter-spacing:.04em;color:var(--ink)}
  .fax-fields{position:absolute;left:24px;right:24px;top:128px;display:grid;grid-template-columns:1fr 1fr;column-gap:16px;font-size:6.5px;color:var(--muted)}
  .fax-fields span{display:block;border-bottom:1px solid var(--rule);padding:7px 0 3px}
  .fax-options{position:absolute;left:24px;right:24px;top:232px;display:flex;justify-content:space-between;font-size:6px;color:var(--muted)}
  .fax-options span::before{content:"";display:inline-block;width:6px;height:6px;border:1px solid var(--muted);border-radius:50%;margin-right:3px;vertical-align:-1px}
  .fax-divider{position:absolute;left:24px;right:24px;top:224px;border-top:1px solid var(--rule)}
</style>
</head>
<body>

<!-- business cards -->
<div class="piece card card-front">
  <div class="brand" style="left:12px;top:14px;font-size:9px"><i class="mark" style="width:10px;height:10px"></i>Bram Keswick</div>
  <div class="tagline" style="left:26px;top:27px;color:var(--muted)">Publishing Solutions, LLC</div>
  <svg class="band" style="bottom:0;height:30px" viewBox="0 0 200 30" preserveAspectRatio="none">
    <path d="M0 22 C70 4 140 26 200 6 V30 H0Z" fill="var(--silver)"/>
    <path d="M0 28 C80 12 140 30 200 14 V30 H0Z" fill="var(--royal)"/>
  </svg>
</div>

<div class="piece card card-back">
  <div class="contact"><strong>Lyle R. Pennock</strong><br>President/Managing Editor<br>478 Birchfield Hollow Road<br>Valencia, PA 16874<br>P 724.555.0148<br>lyle.pennock@bramkeswickbooks.example</div>
  <div class="brand" style="right:10px;top:9px;font-size:7px"><i class="mark" style="width:8px;height:8px"></i>BKS</div>
  <svg class="band" style="bottom:0;height:26px" viewBox="0 0 214 26" preserveAspectRatio="none">
    <path d="M0 20 C80 2 150 22 214 4 V26 H0Z" fill="var(--silver)"/>
    <path d="M0 26 C90 10 150 26 214 12 V26Z" fill="var(--royal)"/>
  </svg>
</div>

<div class="piece card card-navy">
  <div class="brand light" style="left:40px;top:30px;font-size:11px"><i class="mark" style="width:11px;height:11px"></i>Bram Keswick</div>
  <div class="tagline" style="left:58px;top:46px;color:#c9d0ff">Publishing Solutions, LLC</div>
</div>

<div class="piece card card-slate">
  <div class="brand light" style="left:50px;top:28px;font-size:10px"><i class="mark" style="width:10px;height:10px"></i>Bram Keswick</div>
  <div class="tagline" style="left:66px;top:43px;color:#d6d8dd">Publishing Solutions, LLC</div>
</div>

<!-- envelopes -->
<div class="piece env env-plain">
  <svg class="band" style="top:0;height:92px" viewBox="0 0 266 92" preserveAspectRatio="none">
    <path d="M190 0 H266 V40 C240 20 215 10 190 0Z" fill="var(--royal)"/>
    <path d="M170 0 H190 C215 10 240 20 266 40 V48 C235 26 205 12 170 0Z" fill="var(--silver)"/>
  </svg>
</div>

<div class="piece env env-slate">
  <svg class="band" style="top:0;height:104px" viewBox="0 0 272 104" preserveAspectRatio="none">
    <path d="M0 0 H272 V30 C180 60 90 20 0 40Z" fill="#3c3e44"/>
    <path d="M0 40 C90 20 180 60 272 30 V36 C180 66 90 26 0 46Z" fill="var(--silver)"/>
    <path d="M200 104 C230 80 250 70 272 66 V104Z" fill="var(--navy)"/>
  </svg>
</div>

<div class="piece env env-return">
  <div class="brand" style="left:12px;top:46px;font-size:8px"><i class="mark" style="width:8px;height:8px"></i>Bram Keswick</div>
  <div class="return">478 Birchfield Hollow Road<br>Valencia, PA 16874</div>
  <svg class="band" style="top:0;height:92px" viewBox="0 0 266 92" preserveAspectRatio="none">
    <path d="M180 0 H266 V26 C236 14 208 6 180 0Z" fill="var(--silver)"/>
  </svg>
</div>

<!-- letterhead -->
<div class="piece letterhead">
  <svg class="band" style="top:0;height:96px" viewBox="0 0 388 96" preserveAspectRatio="none">
    <defs>
      <linearGradient id="lh-blue" x1="0" y1="0" x2="1" y2="0">
        <stop offset="0" stop-color="var(--navy)"/><stop offset=".7" stop-color="var(--royal)"/><stop offset="1" stop-color="var(--bright)"/>
      </linearGradient>
    </defs>
    <path d="M0 0 H388 V70 C260 40 130 50 0 86Z" fill="var(--silver)"/>
    <path d="M0 0 H388 V60 C260 30 130 40 0 76Z" fill="url(#lh-blue)"/>
  </svg>
  <div class="brand light" style="left:138px;top:18px;font-size:12px"><i class="mark" style="width:12px;height:12px"></i>Bram Keswick</div>
  <div class="watermark">Bram Keswick</div>
</div>

<!-- fax cover -->
<div class="piece fax">
  <svg class="band" style="top:0;height:96px" viewBox="0 0 360 96" preserveAspectRatio="none">
    <defs>
      <linearGradient id="fx-blue" x1="0" y1="0" x2="1" y2="0">
        <stop offset="0" stop-color="var(--navy)"/><stop offset=".7" stop-color="var(--royal)"/><stop offset="1" stop-color="var(--bright)"/>
      </linearGradient>
    </defs>
    <path d="M0 0 H360 V70 C240 40 120 50 0 86Z" fill="var(--silver)"/>
    <path d="M0 0 H360 V60 C240 30 120 40 0 76Z" fill="url(#fx-blue)"/>
  </svg>
  <div class="brand light" style="left:126px;top:18px;font-size:12px"><i class="mark" style="width:12px;height:12px"></i>Bram Keswick</div>
  <div class="fax-title">FAX</div>
  <div class="fax-fields">
    <span>TO:</span><span>FROM:</span>
    <span>FAX:</span><span>PAGES:</span>
    <span>PHONE:</span><span>DATE:</span>
    <span>RE:</span><span>CC:</span>
  </div>
  <div class="fax-divider"></div>
  <div class="fax-options">
    <span>Urgent</span><span>For Review</span><span>Please comment</span><span>Please reply</span><span>Please recycle</span>
  </div>
</div>

</body>
</html>
```